Harbor Mortgage Relief

Please help us give our website a remake or a FACELIFT. It is not very good but it says what we need it to say. But the design is terrible.
I would like our new design font and logo to be used as the theme.

I also want more photos on the site.

I also want consistency with the pages so they look clean.

We want the professionals to do this, let's see what you got!

Thank you!
Updates

Project Deadline Extended
Reason: I can understand you want to be paid. So I will commit to the fee but I want you to have time to make a KICK ASS website for me dudes! Thanks

HI!  Just wanted to say thanks for your time on these.  A lot are great.  However the firefighters have nothing to do with Foreclosure.  We are saving peoples homes from the bank taking them and selling them.   I LOVE the house photos and the families on the website.  That is the direction we like.  THanks.

THANK U ALL FOR THE WORK!   I like a few ending in the numbers: 147  733  693  536  620  478  727  508     I will go over them and choose one soon.  Thank you.   You will be paid shortly. 

Requirements
Must have
• Bright, Upbeat photos. Color scheme should be in order. We like icons on the bottom. not just text.

```html
<!DOCTYPE html>
<html lang="en">
<head>
<meta charset="utf-8">
<title>Harbor Mortgage Relief</title>
<link href="https://fonts.googleapis.com/css2?family=Roboto+Condensed:wght@400;700&family=Arimo:wght@400;700&display=swap" rel="stylesheet">
<style>
:root{
  --red:#c8120e;
  --red-dark:#9a0a07;
  --page:#2b2b2b;
  --topbar:#1b1b1b;
  --footer:#171717;
  --white:#ffffff;
  --soft:#f4f4f4;
  --text:#6f6f6f;
  --ink:#1a1a1a;
  --line:#d2d2d2;
}
*{margin:0;padding:0;box-sizing:border-box}
html,body{width:1187px;height:1200px;overflow:hidden}
body{background:var(--page);font-family:"Roboto Condensed",sans-serif;color:var(--ink)}

/* top bar */
.topbar{height:34px;background:var(--topbar);display:flex;justify-content:flex-end;align-items:center;gap:8px;padding:0 25px}
.topbar span{width:22px;height:22px;border-radius:3px;background:#5a5a5a;display:block}

/* header */
.site-header{height:86px;background:var(--white);display:flex;align-items:center;justify-content:space-between;padding:0 25px}
.brand{display:flex;align-items:center;gap:14px;font-weight:700;font-size:30px;color:var(--red);text-transform:uppercase;letter-spacing:.3px}
.brand-dot{width:54px;height:54px;border-radius:50%;background:var(--red);flex:none}
.callout{text-align:right;line-height:1}
.callout .label{display:block;font-size:16px;color:var(--text);letter-spacing:1px;margin-bottom:4px}
.callout .number{font-size:36px;font-weight:700;color:var(--red)}

/* nav */
.main-nav{height:48px;background:var(--red);border-bottom:3px solid var(--red-dark);display:flex;align-items:center;justify-content:space-between;padding:0 25px}
.main-nav ul{list-style:none;display:flex;gap:6px}
.main-nav li{font-size:18px;color:var(--white);padding:0 16px;line-height:34px;border-radius:3px}
.main-nav li.active{background:var(--white);color:var(--red);font-weight:700}
.search{display:flex;width:240px;height:30px;background:var(--white);border-radius:3px;overflow:hidden}
.search span{flex:1;font-family:"Arimo",sans-serif;font-size:14px;color:#777;line-height:30px;padding-left:10px}
.search i{width:32px;background:var(--ink);display:flex;align-items:center;justify-content:center}

/* hero */
.hero{height:318px;background:var(--page);display:flex;gap:20px;padding:14px 25px}
.slide{position:relative;width:750px;height:290px;border-radius:4px;overflow:hidden;
  background:linear-gradient(160deg,#9cc8e8 0%,#cfe6f3 38%,#e9d8b8 60%,#7fa65a 100%)}
.slide-caption{position:absolute;left:0;bottom:0;width:100%;height:58px;background:rgba(20,20,20,.55);color:var(--white);font-size:30px;line-height:58px;padding-left:20px}
.dots{position:absolute;right:18px;bottom:20px;display:flex;gap:6px}
.dots span{width:11px;height:11px;border-radius:50%;background:var(--white)}
.dots span:first-child{background:var(--red)}
.services{width:367px;height:290px;background:var(--white);border-radius:4px;border-top:5px solid var(--red);padding:16px 20px}
.services h2{font-size:28px;font-weight:700;color:var(--red);line-height:1;margin-bottom:10px}
.services-intro{font-size:16px;color:var(--text);line-height:21px;margin-bottom:10px}
.services ul{list-style:none;font-size:16px;line-height:20px}
.services li{position:relative;padding-left:22px;margin-bottom:7px}
.services li svg{position:absolute;left:0;top:3px}

/* content */
.content{height:446px;background:var(--white);margin:0 25px;display:flex;gap:28px;padding:24px 24px 0}
.copy{width:715px}
.copy h1{font-size:28px;font-weight:400;color:var(--red);margin-bottom:10px}
.copy p{font-family:"Arimo",sans-serif;font-size:13.5px;line-height:19px;color:var(--text);margin-bottom:11px}
.copy .name{color:var(--red)}
.gallery{flex:1;display:flex;flex-direction:column;gap:14px}
.photo{height:190px;border-radius:4px}
.photo-home{background:linear-gradient(170deg,#a8d3f0 0%,#e8eef2 45%,#d9c3a0 70%,#6e9a4e 100%)}
.photo-family{background:linear-gradient(150deg,#f3d9b8 0%,#e7b98f 40%,#9fc3de 100%)}

/* footer */
.site-footer{height:264px;background:var(--footer);color:var(--white);padding:30px 25px 0}
.contact-row{display:flex;justify-content:center;gap:40px}
.contact{width:330px;display:flex;gap:14px;align-items:flex-start}
.icon{width:48px;height:48px;border-radius:50%;background:var(--red);display:flex;align-items:center;justify-content:center;flex:none}
.contact h3{font-size:17px;font-weight:700;color:var(--red);text-transform:uppercase;letter-spacing:.5px;margin-bottom:4px}
.contact p{font-size:18px;line-height:23px}
.footer-legal{margin-top:44px;padding-top:16px;border-top:1px solid #333;text-align:center;font-size:14px;color:#bdbdbd}
</style>
</head>
<body>

<div class="topbar"><span></span><span></span><span></span><span></span></div>

<header class="site-header">
  <div class="brand"><span class="brand-dot"></span><span>Harbor Mortgage Relief</span></div>
  <div class="callout"><span class="label">CALL TOLL FREE NOW</span><span class="number">888.555.0142</span></div>
</header>

<nav class="main-nav">
  <ul>
    <li class="active">Home</li>
    <li>About Us</li>
    <li>Services</li>
    <li>Financing Options</li>
    <li>Contact Us</li>
  </ul>
  <div class="search"><span>Search</span><i><svg width="16" height="16" viewBox="0 0 16 16"><circle cx="9" cy="7" r="4.5" fill="none" stroke="#fff" stroke-width="2"/><line x1="5.5" y1="10.5" x2="2" y2="14" stroke="#fff" stroke-width="2.4"/></svg></i></div>
</nav>

<section class="hero">
  <div class="slide" role="img" aria-label="Bright photo of a smiling family in front of their home">
    <div class="slide-caption">Lorem Ipsum is simply</div>
    <div class="dots"><span></span><span></span><span></span></div>
  </div>
  <aside class="services">
    <h2>Our Services</h2>
    <p class="services-intro">Some of the solutions our specialist can discuss with you are:</p>
    <ul>
      <li><svg width="14" height="14" viewBox="0 0 14 14"><path d="M2 7l3 3 7-7" fill="none" stroke="#c8120e" stroke-width="2.4"/></svg>Bringing your mortgage current to stop the foreclosure</li>
      <li><svg width="14" height="14" viewBox="0 0 14 14"><path d="M2 7l3 3 7-7" fill="none" stroke="#c8120e" stroke-width="2.4"/></svg>HMR can purchase your home with CASH in 7-10 days</li>
      <li><svg width="14" height="14" viewBox="0 0 14 14"><path d="M2 7l3 3 7-7" fill="none" stroke="#c8120e" stroke-width="2.4"/></svg>Financing/Purchase Options</li>
      <li><svg width="14" height="14" viewBox="0 0 14 14"><path d="M2 7l3 3 7-7" fill="none" stroke="#c8120e" stroke-width="2.4"/></svg>Relocations Assistance - if needed</li>
      <li><svg width="14" height="14" viewBox="0 0 14 14"><path d="M2 7l3 3 7-7" fill="none" stroke="#c8120e" stroke-width="2.4"/></svg>Remodel your home to increase it's value</li>
    </ul>
  </aside>
</section>

<main class="content">
  <div class="copy">
    <h1>Welcome to Harbor Mortgage Relief</h1>
    <p><span class="name">HARBOR MORTGAGE RELIEF</span> specializes in assisting homeowners who are in FORECLOSURE, by offering solid alternatives to losing your home in a Trustee Sale. Having your home foreclosed on can damage your credit for up to 7 years. Most foreclosures end with the home owner being evicted from their home, leaving them with no money, no place to live and without ample time to safely remove their possessions from their home. There is no need to have this happen to you. No matter what part of foreclosure process you are in, WE CAN HELP!</p>
    <p>If you have received a Notice of Default (NOD) or Notice of Trustee Sale (NTS), you have options. Contact us today to speak to one of our licensed specialist, and let us help you put this situation behind you.</p>
    <p>We speak to hundreds of homeowners every day, we understand how frustrating this can be. Don't live in fear of what is to come. You have other options, please call or email us today and we will immediately put our specialist to work finding you a solution.</p>
    <p>Don't try to handle this frustrating situation by yourself. <span class="name">HARBOR MORTGAGE RELIEF</span> is a team of knowledgeable real estate professionals, we can offer you a better solution during this tough time.</p>
    <p>HARBOR MORTGAGE RELIEF has been assisting families in foreclosure for years. Our skill and integrity has earned us a reputation for fast, professional, courteous and thorough solutions. With over 50 years of real estate knowledge and experience HARBOR MORTGAGE RELIEF is ready to assist you.</p>
  </div>
  <div class="gallery">
    <div class="photo photo-home" role="img" aria-label="Photo of a sunny suburban house with a green lawn"></div>
    <div class="photo photo-family" role="img" aria-label="Photo of a happy family relaxing together at home"></div>
  </div>
</main>

<footer class="site-footer">
  <div class="contact-row">
    <div class="contact">
      <span class="icon"><svg width="22" height="26" viewBox="0 0 22 26"><path d="M11 1C5.5 1 2 5 2 9.5 2 16 11 25 11 25s9-9 9-15.5C20 5 16.5 1 11 1z" fill="#fff"/><circle cx="11" cy="9.5" r="3.2" fill="#c8120e"/></svg></span>
      <div><h3>Harbor Mortgage Relief</h3><p>118 Harbor View Drive Suite 210<br>Bayport, CA 90210</p></div>
    </div>
    <div class="contact">
      <span class="icon"><svg width="24" height="24" viewBox="0 0 24 24"><path d="M6.6 2.5l3 3.6-1.9 2.6c1.3 2.8 3.5 5 6.3 6.3l2.6-1.9 3.6 3-1.4 3.6C11 19.6 4.4 13 4.3 4z" fill="#fff"/></svg></span>
      <div><h3>Call Toll Free</h3><p>888-555-0142</p></div>
    </div>
    <div class="contact">
      <span class="icon"><svg width="24" height="24" viewBox="0 0 24 24"><path d="M3 11.5L12 4l9 7.5" fill="none" stroke="#fff" stroke-width="2.2"/><path d="M6 10.5V20h12v-9.5" fill="#fff"/><rect x="10.5" y="14" width="3" height="6" fill="#c8120e"/></svg></span>
      <div><h3>Online</h3><p>HARBORMORTGAGERELIEF.COM</p></div>
    </div>
  </div>
  <p class="footer-legal">Content copyright 2012. HARBORMORTGAGERELIEF.COM. All rights reserved.</p>
</footer>

</body>
</html>
```